Marketing collateral for Northfield Valley Heart and Artery Center
folder, rack card, brochure, other
Marketing collateral for Northfield Valley Heart and Artery Center - Health
Creative Brief
Health
These materials will have a dual focus. They will be used to introduce two physicians to other medical doctors in hopes of getting them to refer patients to them. They will also be used to educate patients/ potential patients of the services that we offer at the practice. It will also provide patients with more information about their doctor.
I want to use only my photos and logos. All of the information I would like is attached, including text. I would need all of the files in an editable format.

```html
<!DOCTYPE html>
<html lang="en">
<head>
<meta charset="utf-8">
<title>Northfield Valley Heart and Artery Center – Presentation Folder</title>
<link href="https://fonts.googleapis.com/css2?family=Tinos&display=swap" rel="stylesheet">
<style>
  :root {
    --backdrop: #d8d3cc;
    --folder-navy: #0f4763;
    --accent-blue: #1f9ad6;
    --paper-white: #ffffff;
    --band-white: #f4f7f9;
    --ink-navy: #0f4763;
  }
  html, body {
    margin: 0;
    padding: 0;
    width: 1200px;
    height: 569px;
    overflow: hidden;
    background: var(--backdrop);
  }
  .folder-spread {
    display: block;
    width: 1200px;
    height: 569px;
    font-family: "Tinos", "Times New Roman", serif;
  }
  .navy { fill: var(--folder-navy); }
  .pocket { fill: var(--folder-navy); }
  .accent { fill: var(--accent-blue); }
  .paper { fill: var(--paper-white); }
  .band { fill: var(--band-white); }
  .brand-name { font-size: 15px; }
  .brand-sub { font-size: 11px; }
  .lockup-on-dark { fill: var(--paper-white); }
  .lockup-on-light { fill: var(--ink-navy); }
  .fine-print { fill: var(--ink-navy); font-size: 7px; }
  .fine-print-light { fill: var(--paper-white); font-size: 7px; }
</style>
</head>
<body>
<svg class="folder-spread" viewBox="0 0 1200 569" xmlns="http://www.w3.org/2000/svg" aria-label="Presentation folder for Northfield Valley Heart and Artery Center, outside and inside">
  <defs>
    <g id="brand-lockup">
      <rect class="accent" x="0" y="0" width="24" height="24" rx="3"/>
      <text class="brand-name" x="30" y="11">Northfield Valley</text>
      <text class="brand-sub" x="30" y="25">Heart &amp; Artery Center</text>
    </g>
  </defs>

  <!-- Outside: cover -->
  <g class="folder-outside">
    <rect class="navy" x="24" y="24" width="576" height="408"/>
    <rect class="accent cover-mark" x="108" y="144" width="84" height="84" rx="12"/>
    <rect class="band" x="24" y="346" width="576" height="46"/>
    <text class="fine-print" x="36" y="372">210 Orchard Lane, Suite 4, Northfield</text>
    <use class="lockup-on-light" href="#brand-lockup" x="338" y="354"/>

    <!-- Pocket flaps, printed upside down -->
    <path class="navy" d="M24 432 H300 C300 468 282 470 282 500 V540 Q282 552 270 552 H48 Q24 552 24 528 Z"/>
    <path class="navy" d="M600 432 V528 Q600 552 576 552 H342 Q330 552 330 540 V500 C330 470 312 468 312 432 Z"/>
    <g transform="rotate(180 150 492)">
      <use class="lockup-on-dark" href="#brand-lockup" x="88" y="480"/>
    </g>
    <g transform="rotate(180 470 492)">
      <use class="lockup-on-dark" href="#brand-lockup" x="408" y="480"/>
    </g>
  </g>

  <!-- Inside: pockets -->
  <g class="folder-inside">
    <rect class="paper" x="612" y="24" width="564" height="528"/>
    <rect class="navy" x="612" y="24" width="564" height="108"/>
    <use class="lockup-on-dark" href="#brand-lockup" x="636" y="40"/>
    <text class="fine-print-light" x="1160" y="108" text-anchor="end">Northfield, Valley 20117</text>

    <path class="pocket" d="M612 360 H860 Q884 360 884 384 V552 H612 Z"/>
    <path class="pocket" d="M1176 360 H920 Q896 360 896 384 V552 H1176 Z"/>
    <use class="lockup-on-dark" href="#brand-lockup" x="648" y="456"/>
    <use class="lockup-on-dark" href="#brand-lockup" x="1010" y="456"/>
  </g>
</svg>
</body>
</html>
```